Quiet Harbor - Childhood Cancer Journey

In 2019, Tovin, my five-year-old, was diagnosed with stage 4 kidney cancer.

From the beginning, I said God would do his part, the doctors will do theirs, and I would do mine to save my son.

Diving into Christian beliefs and research, I learned and applied major shifts in everything we didn’t. Pulling invaluable information from fields like alternative cancer treatments coupled with Corvel Ring study, Longevity, Biohacking, Functional Medicine, and microbiome.

Tovin when from stage 4 to cancer-free in 8 months. The journey is and was very difficult, but we’ve learned and been able to help countless others.

Industry/Entity Type

Health, Wellness, Mindset, Adversity

Requirements
Nice to have
• Bright with feelings of warmth

```html
<!DOCTYPE html>
<html lang="en">
<head>
<meta charset="UTF-8">
<title>Quiet Harbor – Book Cover</title>
<link href="https://fonts.googleapis.com/css2?family=Poppins:wght@400;500;600&display=swap" rel="stylesheet">
<style>
  :root {
    --page-bg: #e9e7e4;
    --cover-bg: #ffffff;
    --title-dark: #2b2b2b;
    --title-red: #e31e2d;
    --heart-red: #d9141f;
    --heart-deep: #a50d16;
    --photo-red: #d8283a;
    --photo-pink: #c9306a;
    --photo-grey: #7c7a78;
    --author-ink: #111111;
    --subtitle-ink: #ffffff;
  }
  * { margin: 0; padding: 0; box-sizing: border-box; }
  html, body {
    width: 1200px;
    height: 1200px;
    overflow: hidden;
    background: var(--page-bg);
  }
  .stage {
    width: 1200px;
    height: 1200px;
    display: flex;
    align-items: center;
    justify-content: center;
  }
  .cover {
    position: relative;
    width: 774px;
    height: 1160px;
    background: var(--cover-bg);
    box-shadow: 0 10px 30px rgba(0,0,0,0.18);
    font-family: "Poppins", sans-serif;
    overflow: hidden;
  }
  .title {
    position: absolute;
    top: 48px;
    left: 0;
    right: 0;
    text-align: center;
    line-height: 0.86;
  }
  .title-top {
    display: block;
    font-weight: 500;
    font-size: 176px;
    letter-spacing: -4px;
    color: var(--title-dark);
  }
  .title-bottom {
    display: block;
    font-weight: 600;
    font-size: 158px;
    letter-spacing: -5px;
    color: var(--title-red);
  }
  .photo {
    position: absolute;
    left: 262px;
    top: 350px;
    width: 268px;
    height: 340px;
    border-radius: 110px 110px 10px 10px;
    background:
      radial-gradient(ellipse at 70% 30%, var(--photo-grey) 0 22%, transparent 40%),
      linear-gradient(160deg, var(--photo-red) 0%, var(--photo-pink) 70%, #b82a55 100%);
  }
  .heart {
    position: absolute;
    left: 170px;
    top: 600px;
    width: 440px;
    height: 400px;
  }
  .subtitle {
    position: absolute;
    left: 230px;
    top: 690px;
    width: 320px;
    text-align: center;
    color: var(--subtitle-ink);
    font-weight: 500;
    font-size: 19px;
    line-height: 1.22;
    transform: rotate(4deg);
  }
  .author {
    position: absolute;
    left: 0;
    right: 0;
    bottom: 52px;
    text-align: center;
    font-weight: 500;
    font-size: 66px;
    letter-spacing: 1px;
    color: var(--author-ink);
  }
</style>
</head>
<body>
  <main class="stage">
    <section class="cover">
      <h1 class="title">
        <span class="title-top">QUIET</span>
        <span class="title-bottom">HARBOR</span>
      </h1>

      <div class="photo" role="img" aria-label="Photo of a father in a cap embracing his young son in a red shirt"></div>

      <svg class="heart" viewBox="0 0 440 400" aria-hidden="true">
        <defs>
          <radialGradient id="heartFill" cx="50%" cy="40%" r="65%">
            <stop offset="0%" stop-color="var(--heart-red)"/>
            <stop offset="100%" stop-color="var(--heart-deep)"/>
          </radialGradient>
        </defs>
        <path d="M220 380 C 120 310, 18 230, 18 130 C 18 60, 70 18, 130 18 C 175 18, 205 45, 220 75 C 235 45, 265 18, 310 18 C 370 18, 422 60, 422 130 C 422 230, 320 310, 220 380 Z"
              fill="url(#heartFill)" stroke="#ffffff" stroke-width="14" stroke-linejoin="round"/>
      </svg>

      <p class="subtitle">A Loving Father, Determined to Guide His Cancer-Stricken Son’s Journey to a Cure, Discovers the Corvel Ring Protocol of Nourishing the Body to Optimum Health</p>

      <p class="author">MAREK HALLOWAY</p>
    </section>
  </main>
</body>
</html>
```